Business cards, envelopes, etc. for real estate company

We have a finished logo for our real estate company. We need a corporate identity package with the following items:

1. Business Cards
2. Letterhead/Stationary - with 2 pages:
-1st page with full header
-2nd page without top header
3. Concise and professional e-mail signature image
4. Fax coversheet
5. Shipping label, with our return address and a mail-to address (on one label)

We need these to be editable. We don't know the industry standard for these items but perhaps you can provide them to us in .PDF and Word format (and if you use Adobe Illustrator for them, .AI as well).

Please use the attached placeholder logo in your design entry. We will provide you with the original logo to swap in (same size and design, just different text) when we choose your entry.

Please include the following information on the letterhead and business cards:

58 Birchwell Road
Suite 2B West
New York, NY 10587

Tel: 555-014-2837
Fax :555-014-2837

Please contact us if you have any questions about this contest.

Hi,

Thanks for your interest in this project. The logo to use should be working now. Please contact me if you have any further issues or questions.

I look forward to seeing your submissions. 

Hi,

We first wish to thank you all for your submissions. 

Here is some general feedback regarding the designs shown:

1. We would prefer square (as opposed to rounded) business cards.

2. For the fax coversheets, we are looking with a designed look. While we understand these are samples, we don't want it to appear as if it a standard block of text or a fax template from a word processing program.

3. For the 1st page of letterhead and envelopes, we do need an office address on them. The envelopes should have space for a stamp in the top right corner. We would prefer the envelopes not to have colored stripes.

4. We think a watermark of the logo is an interesting idea on the business cards and/or letterhead. This may be something to try. However, it is not strictly necessary and we would like to evaluate designs with and without it.

In general we are looking for a clean yet professional look.

We are actively reviewing all entries and thank you for your time and creativity.

One last comment: We understand making all objects in the brief takes some time. However, we want to remind all the designers that this contest is for more than just business cards (envelopes, letterheads, etc.) so if we choose your design, those items will be expected. Please refer to the original brief to see what we are requesting.

If you provide a mockup of any item listed in the brief (in addition to business cards) it would help us visualize your entire vision for this project.

```html
<!DOCTYPE html>
<html lang="en">
<head>
<meta charset="utf-8">
<title>Harwell &amp; Harwell — Business Cards</title>
<link href="https://fonts.googleapis.com/css2?family=Lato:wght@300;400;700&display=swap" rel="stylesheet">
<style>
  :root {
    --backdrop: #dedcdc;
    --paper: #f6f5f4;
    --teal: #1d5568;
    --ink-grey: #7c7f83;
    --ink-dark: #3a3d40;
    --rule: #8a8d90;
  }
  * { box-sizing: border-box; margin: 0; padding: 0; }
  html, body {
    width: 1200px; height: 845px; overflow: hidden;
    background: var(--backdrop);
    font-family: "Lato", Arial, sans-serif;
  }
  .stage { position: relative; width: 1200px; height: 845px; }

  .card {
    position: absolute;
    width: 520px; height: 297px;
    background: var(--paper);
    box-shadow: 0 6px 18px rgba(0,0,0,0.12);
  }
  .card--front { left: 50px; top: 274px; border: 16px solid var(--teal); }
  .card--back  { left: 630px; top: 274px; }

  .brand { display: flex; align-items: center; gap: 16px; }
  .brand__square { background: var(--teal); flex: none; }
  .brand__name {
    font-weight: 300; color: var(--ink-grey); line-height: 0.95;
  }

  .card--front .brand {
    position: absolute; left: 50%; top: 50%;
    transform: translate(-50%, -50%);
  }
  .card--front .brand__square { width: 74px; height: 74px; }
  .card--front .brand__name { font-size: 44px; }

  .card--back .brand { position: absolute; left: 34px; top: 34px; gap: 14px; }
  .card--back .brand__square { width: 58px; height: 58px; }
  .card--back .brand__name { font-size: 34px; }

  .holder { position: absolute; left: 34px; top: 178px; }
  .holder__name { font-size: 24px; font-weight: 400; color: var(--ink-dark); }
  .holder__title { font-size: 14px; font-weight: 400; color: var(--ink-grey); margin-top: 4px; }

  .divider {
    position: absolute; left: 296px; top: 118px;
    width: 1px; height: 112px; background: var(--rule);
  }

  .contact {
    position: absolute; left: 310px; top: 116px;
    list-style: none; font-size: 12.5px; color: var(--ink-dark); line-height: 1.35;
  }
  .contact li { display: flex; align-items: center; gap: 7px; }
  .contact svg { width: 13px; height: 13px; flex: none; }
  .contact .web { font-weight: 700; color: var(--teal); }
  .contact .address { margin-top: 8px; padding-left: 20px; display: block; }
</style>
</head>
<body>
<main class="stage">

  <section class="card card--front" aria-label="Business card front">
    <div class="brand">
      <span class="brand__square"></span>
      <span class="brand__name">Harwell<br>&amp; Harwell</span>
    </div>
  </section>

  <section class="card card--back" aria-label="Business card back">
    <div class="brand">
      <span class="brand__square"></span>
      <span class="brand__name">Harwell<br>&amp; Harwell</span>
    </div>

    <div class="holder">
      <p class="holder__name">Nadia Corwin</p>
      <p class="holder__title">Operation Manager</p>
    </div>

    <span class="divider"></span>

    <ul class="contact">
      <li>
        <svg viewBox="0 0 14 14" aria-label="Phone"><rect x="1" y="3" width="12" height="9" rx="1" fill="none" stroke="#1d5568" stroke-width="1.4"/><rect x="3" y="1" width="8" height="3" fill="#1d5568"/><rect x="4" y="6" width="6" height="4" fill="#1d5568"/></svg>
        <span>555-014-2837</span>
      </li>
      <li>
        <svg viewBox="0 0 14 14" aria-label="Fax"><rect x="3" y="1" width="8" height="5" fill="none" stroke="#1d5568" stroke-width="1.4"/><rect x="1" y="6" width="12" height="6" rx="1" fill="#1d5568"/></svg>
        <span>555-014-2837</span>
      </li>
      <li>
        <svg viewBox="0 0 14 14" aria-label="Web"><rect x="3.5" y="1" width="7" height="12" rx="3.5" fill="none" stroke="#1d5568" stroke-width="1.4"/><line x1="7" y1="2" x2="7" y2="6" stroke="#1d5568" stroke-width="1.4"/></svg>
        <span class="web">www.harwell-harwell.com</span>
      </li>
      <li class="address">58 Birchwell Road, Suite 2B West,<br>New York, NY 10587</li>
    </ul>
  </section>

</main>
</body>
</html>
```